Biz Card for Harrowfield Property Partners - HWPP

Harrowfield Property Partners is a commercial real estate acquisitions firm. We buy commercial property and need to raise capital from investors for each deal we buy. The vibe needs to be: give us your money, we will multiply it.
Our website: www.hrwpp-example.com
Competitors are: https://velmarholdings-example.com/, https://tribanquepartners-example.com/, http://www.ostrellecapital-example.com/
Target Market(s)
High Net Worth Individuals, Bankers, Insurance Companies, Commercial Real Estate Brokers.
Industry/Entity Type
Investment Banking
Contact Information for Business Card
Name, Title, Addess, Cell#, Office#, email, website
Requirements
Must have
- use one of our logos. See website for look and feel: www.hrwpp-example.com
Nice to have
- see website: www.hrwpp-example.com

```html
<!DOCTYPE html>
<html lang="en">
<head>
<meta charset="utf-8">
<title>Harrowfield Property Partners – Business Card</title>
<link rel="stylesheet" href="https://fonts.googleapis.com/css2?family=Lato:wght@300;400&family=Montserrat:wght@300;400;500;700&display=swap">
<style>
  :root {
    --backdrop: #b7b7b7;
    --navy: #132a47;
    --navy-deep: #0f2440;
    --accent: #3a86c4;
    --paper: #f5f6f7;
    --ink-light: #ffffff;
    --muted: #5f7d99;
  }
  * { box-sizing: border-box; margin: 0; padding: 0; }
  html, body {
    width: 1200px; height: 900px; overflow: hidden;
    background: var(--backdrop);
  }
  .canvas {
    position: relative; width: 1200px; height: 900px;
  }
  .card {
    position: absolute; left: 390px; width: 420px; height: 240px;
    overflow: hidden;
  }
  /* Front: contact side */
  .card-front { top: 185px; background: var(--navy); }
  .card-front .brand-band {
    height: 90px; background: var(--paper);
    display: flex; align-items: center; justify-content: center; gap: 12px;
  }
  .brand-dot {
    width: 52px; height: 52px; border-radius: 50%;
    background: var(--navy); flex: none;
  }
  .brand-name {
    font-family: "Lato", sans-serif; font-weight: 400;
    color: var(--navy); font-size: 15px; letter-spacing: 0.22em;
    line-height: 1.35; text-transform: uppercase;
  }
  .contact-panel {
    position: absolute; top: 90px; left: 0; right: 0; bottom: 0;
    background: linear-gradient(160deg, #183556 0%, var(--navy-deep) 100%);
  }
  .contact-frame {
    position: absolute; inset: 6px 2px 5px 3px;
    border: 1px solid var(--accent);
  }
  .icon-strip {
    position: absolute; left: 38px; top: 39px; width: 21px; height: 83px;
    background: var(--paper);
    display: flex; flex-direction: column; align-items: center;
    justify-content: space-around; padding: 4px 0;
  }
  .icon-strip svg { width: 11px; height: 11px; fill: var(--navy-deep); }
  .contact-list {
    position: absolute; left: 66px; top: 43px; list-style: none;
    font-family: "Montserrat", sans-serif; font-weight: 500;
    color: var(--ink-light); font-size: 10.5px; letter-spacing: 0.03em;
  }
  .contact-list li { height: 19px; line-height: 19px; }
  .person {
    position: absolute; left: 277px; top: 33px; width: 106px;
    font-family: "Montserrat", sans-serif; color: var(--ink-light);
  }
  .person-name { font-size: 16px; line-height: 1; white-space: nowrap; }
  .person-name .first { font-weight: 700; }
  .person-name .last { font-weight: 300; }
  .person-title { font-size: 7px; font-weight: 500; margin-top: 2px; letter-spacing: 0.04em; }
  .person-rule {
    position: relative; margin-top: 6px; height: 1px; background: #dfe7ef;
  }
  .person-rule::before {
    content: ""; position: absolute; left: 0; top: -1px;
    width: 18px; height: 3px; background: var(--accent);
  }
  /* Back: brand side */
  .card-back {
    top: 480px;
    background: linear-gradient(180deg, #142b49 0%, var(--navy-deep) 100%);
    display: flex; align-items: center; padding-left: 52px; gap: 16px;
  }
  .card-back .brand-dot { width: 68px; height: 68px; background: var(--ink-light); }
  .card-back .brand-name { color: var(--ink-light); font-size: 19px; letter-spacing: 0.2em; }
</style>
</head>
<body>
<main class="canvas">
  <section class="card card-front">
    <header class="brand-band">
      <span class="brand-dot"></span>
      <p class="brand-name">Harrowfield<br>Property Partners</p>
    </header>
    <div class="contact-panel">
      <div class="contact-frame"></div>
      <div class="icon-strip">
        <svg viewBox="0 0 24 24" aria-label="Address"><path d="M12 2a7 7 0 0 0-7 7c0 5.2 7 13 7 13s7-7.8 7-13a7 7 0 0 0-7-7zm0 9.5A2.5 2.5 0 1 1 12 6.5a2.5 2.5 0 0 1 0 5z"/></svg>
        <svg viewBox="0 0 24 24" aria-label="Phone"><path d="M6.6 10.8a15.2 15.2 0 0 0 6.6 6.6l2.2-2.2a1 1 0 0 1 1-.25 11.4 11.4 0 0 0 3.6.57 1 1 0 0 1 1 1V20a1 1 0 0 1-1 1A17 17 0 0 1 3 4a1 1 0 0 1 1-1h3.5a1 1 0 0 1 1 1c0 1.25.2 2.45.57 3.6a1 1 0 0 1-.25 1z"/></svg>
        <svg viewBox="0 0 24 24" aria-label="Email"><path d="M2 5h20v14H2zm2 2v.5l8 5.5 8-5.5V7zm0 3v7h16v-7l-8 5.5z"/></svg>
        <svg viewBox="0 0 24 24" aria-label="Website"><path d="M6 2l13 12h-6.5l3.5 7.5-2.6 1.2-3.5-7.6L6 19.5z"/></svg>
      </div>
      <ul class="contact-list">
        <li>123 Dummy, Lorem Ipsum</li>
        <li>+00 1234 5XXX 9012</li>
        <li>info@email space</li>
        <li>www websiteaddress</li>
      </ul>
      <div class="person">
        <p class="person-name"><span class="first">YOUR</span> <span class="last">NAME</span></p>
        <p class="person-title">Co-Founder</p>
        <div class="person-rule"></div>
      </div>
    </div>
  </section>

  <section class="card card-back">
    <span class="brand-dot"></span>
    <p class="brand-name">Harrowfield<br>Property Partners</p>
  </section>
</main>
</body>
</html>
```